Umgestaltung Fragebogen für Betreuungskraftvermittler
Zielgruppe
Wir vermitteln Betreuungskräfte für hilfebedürftige Personen. Unsere Zielgruppe sind meist die Kinder oder Verwandte von Senioren
Aufgabenstellung
Da unser CI noch nicht fertig ist, brauchen wir Platzhalter für unser Logo und unsere Farben sollte im Nachgang noch angepasst werden können. Daher wäre es gut, wenn wir (zB. in Word) im Nachgang noch Schriftart oder Farbe ändern können.
Anbei ein Fragebogen mit kleinen Änderungen - Diese Fragen müssen für die Anamnese enthalten sein.
Der Anamnesebogen soll von Interessenten per PDF ausgedruckt und ausgefüllt werden.

```html
<!DOCTYPE html>
<html lang="de">
<head>
<meta charset="utf-8">
<title>Allgemeine Angaben – Fragebogen</title>
<link rel="stylesheet" href="https://fonts.googleapis.com/css2?family=Noto+Sans:wght@400;700&display=swap">
<style>
  :root {
    --ink: #111111;
    --accent: #d2232a;
    --paper: #ffffff;
    --badge: #4caf3a;
    --rule: #333333;
  }
  * { box-sizing: border-box; margin: 0; padding: 0; }
  html, body { width: 873px; height: 1200px; overflow: hidden; background: var(--paper); }
  body { font-family: "Noto Sans", Verdana, sans-serif; color: var(--ink); font-size: 12px; }
  .sheet { position: relative; width: 873px; height: 1200px; }
  .abs { position: absolute; }

  .title-band {
    left: 0; top: 23px; width: 529px; height: 54px;
    background: var(--ink); border-bottom-right-radius: 12px;
    color: var(--paper); font-weight: 700; font-size: 27px;
    padding-left: 129px; line-height: 54px;
  }
  .logo-box {
    left: 609px; top: 0; width: 264px; height: 102px; background: var(--ink);
    color: var(--paper); font-weight: 700; font-size: 78px; line-height: 102px; text-align: center;
  }
  .intro { left: 108px; top: 129px; font-weight: 700; font-size: 11.5px; line-height: 17px; }

  .section-title { left: 110px; font-weight: 700; font-size: 17px; color: var(--accent); }
  .label { font-size: 12px; line-height: 16px; }
  .line { height: 0; border-bottom: 1px solid var(--rule); }
  .box { display: inline-block; width: 11px; height: 11px; border: 1.5px solid var(--ink); vertical-align: -1px; margin-right: 8px; }
  .check { font-size: 12px; line-height: 16px; white-space: nowrap; }
  .strong { font-weight: 700; }
  .unit { border-bottom: 1px solid var(--rule); width: 50px; text-align: right; }
  .italic { font-style: italic; }

  .footer { left: 0; width: 873px; text-align: center; font-size: 12px; }
  .page-badge {
    left: 826px; top: 1146px; width: 46px; height: 46px; border-radius: 50%;
    background: var(--badge); color: var(--paper); font-size: 17px; line-height: 46px; text-align: center;
  }
</style>
</head>
<body>
<div class="sheet">
  <div class="abs title-band">Allgemeine Angaben</div>
  <div class="abs logo-box">Logo</div>

  <p class="abs intro">Dieses Formular können Sie ausdrucken, ausfüllen und unterschreiben an unsere Kontaktdaten versenden.<br>Es besteht auch die Möglichkeit das Formular online auszufüllen.</p>

  <!-- Abschnitt 1 -->
  <h2 class="abs section-title" style="top:202px">1. Angaben zur Kontaktperson (Auftraggeber)</h2>
  <span class="abs check" style="left:675px;top:206px"><i class="box"></i>Frau</span>
  <span class="abs check" style="left:747px;top:206px"><i class="box"></i>Herr</span>

  <span class="abs label" style="left:129px;top:248px">Name</span><div class="abs line" style="left:176px;top:263px;width:254px"></div>
  <span class="abs label" style="left:481px;top:248px">Vorname</span><div class="abs line" style="left:546px;top:263px;width:254px"></div>
  <span class="abs label" style="left:129px;top:281px">Straße</span><div class="abs line" style="left:176px;top:296px;width:254px"></div>
  <span class="abs label" style="left:481px;top:281px">PLZ / Ort</span><div class="abs line" style="left:546px;top:296px;width:254px"></div>
  <span class="abs label" style="left:129px;top:312px">Telefon</span><div class="abs line" style="left:176px;top:327px;width:254px"></div>
  <span class="abs label" style="left:481px;top:312px">Fax</span><div class="abs line" style="left:546px;top:327px;width:254px"></div>
  <span class="abs label" style="left:129px;top:345px">E-Mail</span><div class="abs line" style="left:176px;top:360px;width:254px"></div>
  <span class="abs label" style="left:129px;top:387px">Verwandtschaftsgrad zu der zu betreuenden Person</span><div class="abs line" style="left:454px;top:401px;width:346px"></div>

  <!-- Abschnitt 2 -->
  <h2 class="abs section-title" style="top:454px">2. Angaben zur zu betreuenden Person (Leistungsempfänger)</h2>
  <span class="abs check" style="left:675px;top:458px"><i class="box"></i>Frau</span>
  <span class="abs check" style="left:747px;top:458px"><i class="box"></i>Herr</span>

  <span class="abs label" style="left:129px;top:502px">Name</span><div class="abs line" style="left:205px;top:517px;width:225px"></div>
  <span class="abs label" style="left:481px;top:502px">Vorname</span><div class="abs line" style="left:574px;top:517px;width:226px"></div>
  <span class="abs label" style="left:129px;top:533px">Straße, Nr.</span><div class="abs line" style="left:205px;top:548px;width:225px"></div>
  <span class="abs label" style="left:481px;top:533px">PLZ / Ort</span><div class="abs line" style="left:574px;top:548px;width:226px"></div>
  <span class="abs label" style="left:129px;top:566px">Telefon</span><div class="abs line" style="left:205px;top:581px;width:225px"></div>
  <span class="abs label" style="left:481px;top:566px">Geburtsdatum</span><div class="abs line" style="left:574px;top:581px;width:226px"></div>
  <span class="abs label" style="left:129px;top:598px">Größe</span><span class="abs label unit" style="left:205px;top:598px">cm</span>
  <span class="abs label" style="left:481px;top:598px">Gewicht</span><span class="abs label unit" style="left:574px;top:598px">kg</span>
  <span class="abs label" style="left:129px;top:631px">Hausarzt</span>
  <div class="abs line" style="left:205px;top:645px;width:595px"></div>
  <div class="abs line" style="left:205px;top:674px;width:595px"></div>

  <!-- Abschnitt 3 -->
  <h2 class="abs section-title" style="top:727px">3. Angaben zur Pflegebedürftigkeit</h2>
  <span class="abs label strong" style="left:146px;top:777px">Pflegegrad</span>
  <span class="abs check" style="left:232px;top:776px"><i class="box"></i>keinen Pflegegrad</span>
  <span class="abs check" style="left:389px;top:776px"><i class="box"></i>1</span>
  <span class="abs check" style="left:466px;top:776px"><i class="box"></i>2</span>
  <span class="abs check" style="left:541px;top:776px"><i class="box"></i>3</span>
  <span class="abs check" style="left:618px;top:776px"><i class="box"></i>4</span>
  <span class="abs check" style="left:694px;top:776px"><i class="box"></i>5</span>
  <span class="abs check" style="left:232px;top:806px"><i class="box"></i>beantragt</span>
  <span class="abs check" style="left:389px;top:806px"><i class="box"></i>1</span>
  <span class="abs check" style="left:466px;top:806px"><i class="box"></i>2</span>
  <span class="abs check" style="left:541px;top:806px"><i class="box"></i>3</span>
  <span class="abs check" style="left:618px;top:806px"><i class="box"></i>4</span>
  <span class="abs check" style="left:694px;top:806px"><i class="box"></i>5</span>

  <p class="abs label strong" style="left:129px;top:882px">Welche Krankheitsbilder sind bekannt (z.B. Schlaganfall, Parkinson, etc.)?</p>

  <span class="abs check" style="left:127px;top:926px"><i class="box"></i>Allergien</span>
  <span class="abs check" style="left:127px;top:945px"><i class="box"></i>altersbedingte Gehschwäche</span>
  <span class="abs check" style="left:127px;top:964px"><i class="box"></i>Alzheimer</span>
  <span class="abs check" style="left:127px;top:984px"><i class="box"></i>Asthma</span>
  <span class="abs check" style="left:127px;top:1003px"><i class="box"></i>chronische Durchfälle</span>
  <span class="abs check" style="left:127px;top:1022px"><i class="box"></i>Demenz (Anfangsstadium)</span>
  <span class="abs check" style="left:127px;top:1041px"><i class="box"></i>Demenz</span>
  <span class="abs check" style="left:127px;top:1060px"><i class="box"></i>Dekubitus</span>

  <span class="abs check" style="left:410px;top:926px"><i class="box"></i>Depression</span>
  <span class="abs check" style="left:410px;top:945px"><i class="box"></i>Diabetes</span>
  <span class="abs check" style="left:410px;top:964px"><i class="box"></i>Diabetes (insulinpflichtig)</span>
  <span class="abs check" style="left:410px;top:984px"><i class="box"></i>Herzinfarkt</span>
  <span class="abs check" style="left:410px;top:1003px"><i class="box"></i>Herzinsuffizienz</span>
  <span class="abs check" style="left:410px;top:1022px"><i class="box"></i>Herzrhythmusstörung</span>
  <span class="abs check" style="left:410px;top:1041px"><i class="box"></i>Hypertonie</span>
  <span class="abs check" style="left:410px;top:1060px"><i class="box"></i>Inkontinenz</span>

  <span class="abs check" style="left:633px;top:926px"><i class="box"></i>multiple Sklerose</span>
  <span class="abs check" style="left:633px;top:945px"><i class="box"></i>Osteoporose</span>
  <span class="abs check" style="left:633px;top:964px"><i class="box"></i>Parkinson</span>
  <span class="abs check" style="left:633px;top:984px"><i class="box"></i>Rheuma</span>
  <span class="abs check" style="left:633px;top:1003px"><i class="box"></i>Schlaganfall <i class="box" style="margin-left:3px"></i>re. <i class="box" style="margin-left:3px"></i>li.</span>
  <span class="abs check" style="left:633px;top:1022px"><i class="box"></i>Stoma (Anus praeter)</span>
  <span class="abs check" style="left:633px;top:1041px"><i class="box"></i>Tumor</span>

  <span class="abs check italic" style="left:127px;top:1099px"><i class="box"></i>Sonstige:</span>
  <div class="abs line" style="left:206px;top:1114px;width:368px"></div>

  <!-- Fußzeile -->
  <p class="abs footer" style="top:1160px">Betreuungsdienst Lindenhof GmbH · Lindenallee 7 · D- 54321 Birkenfeld</p>
  <p class="abs footer" style="top:1180px">Telefon + 49 (0) 54321 / 67890 · Fax: + 49 (0) 54321 / 67891 · E-Mail: kontakt@lindenhof-betreuung.de</p>
  <div class="abs page-badge">1</div>
</div>
</body>
</html>
```